Music Festival Business Cards

The Lantern Gathering
Produced by Bramblewood Sound Collective LLC
New music festival in Arkansas.

Target Market(s)

18-35 year olds

Industry/Entity Type

Festival

Contact Information for Business Card

We are a 5-partner team producing a music festival in Arkansas. We need slick business cards, and I want them to be square.

Requirements
Must have
• I NEED THESE TO BE IN SQUARE SIZE - 2x2 or 2.5x2.5... please not regular size.
• I need www.lanternmeet.example as the link to website.

```html
<!DOCTYPE html>
<html lang="en">
<head>
<meta charset="utf-8">
<title>The Lantern Gathering — Business Cards</title>
<link href="https://fonts.googleapis.com/css2?family=Open+Sans:wght@400;600;700&display=swap" rel="stylesheet">
<style>
  :root {
    --backdrop: #3b3430;
    --card: #0d0d0d;
    --card-edge: #1a1a1a;
    --accent: #3fd0d8;
    --ink: #f2f2f2;
    --silver: #c8c8cc;
    --divider: #262626;
  }
  * { margin: 0; padding: 0; box-sizing: border-box; }
  html, body {
    width: 1200px; height: 900px; overflow: hidden;
    background: var(--backdrop);
    font-family: "Open Sans", Arial, sans-serif;
  }
  .stage {
    position: relative; width: 1200px; height: 900px;
    display: flex; align-items: center; justify-content: center; gap: 60px;
  }
  .card {
    position: relative;
    width: 440px; height: 440px;
    background: var(--card);
    border: 1px solid var(--card-edge);
    box-shadow: 0 14px 30px rgba(0,0,0,0.45);
  }
  /* Front: contact side */
  .card-front { display: flex; align-items: center; }
  .brand-panel {
    width: 48%;
    display: flex; align-items: center; justify-content: center;
    padding: 0 20px;
  }
  .brand-name {
    color: var(--accent);
    font-weight: 700;
    font-size: 26px;
    line-height: 1.15;
    text-transform: uppercase;
    letter-spacing: 1px;
  }
  .info-panel {
    width: 52%;
    border-left: 1px solid var(--divider);
    padding: 12px 0 12px 22px;
    color: var(--ink);
  }
  .person-name {
    color: var(--accent);
    font-weight: 700;
    font-size: 21px;
    line-height: 1.1;
  }
  .person-role { font-size: 13px; margin-top: 3px; }
  .address { font-size: 13px; line-height: 1.4; margin-top: 16px; }
  .contact-list { list-style: none; margin-top: 14px; font-size: 13px; }
  .contact-item { display: flex; align-items: center; gap: 8px; line-height: 1.55; white-space: nowrap; }
  .contact-icon { width: 11px; height: 11px; flex: none; }
  /* Back: name side */
  .card-back { display: flex; align-items: center; justify-content: center; }
  .back-name {
    color: var(--silver);
    font-weight: 600;
    font-size: 26px;
    letter-spacing: 4px;
    text-transform: uppercase;
    text-align: center;
    line-height: 1.3;
  }
</style>
</head>
<body>
<main class="stage">
  <section class="card card-front">
    <div class="brand-panel">
      <div class="brand-name">The Lantern Gathering</div>
    </div>
    <div class="info-panel">
      <h1 class="person-name">Marcus Hale</h1>
      <p class="person-role">Managing Director</p>
      <p class="address">214 Ember Lane,<br>Fayetteville, AR 72701</p>
      <ul class="contact-list">
        <li class="contact-item">
          <svg class="contact-icon" viewBox="0 0 24 24" fill="var(--accent)"><path d="M6.6 10.8a15 15 0 0 0 6.6 6.6l2.2-2.2a1 1 0 0 1 1-.25 11.4 11.4 0 0 0 3.6.57 1 1 0 0 1 1 1V20a1 1 0 0 1-1 1A17 17 0 0 1 3 4a1 1 0 0 1 1-1h3.5a1 1 0 0 1 1 1c0 1.25.2 2.45.57 3.57a1 1 0 0 1-.25 1z"/></svg>
          <span>479-555 0142</span>
        </li>
        <li class="contact-item">
          <svg class="contact-icon" viewBox="0 0 24 24" fill="var(--accent)"><path d="M2 5h20v2l-10 6L2 7zM2 9l10 6 10-6v10H2z"/></svg>
          <span>hello@lanternmeet.example</span>
        </li>
        <li class="contact-item">
          <svg class="contact-icon" viewBox="0 0 24 24" fill="none" stroke="var(--accent)" stroke-width="3" stroke-linecap="round"><path d="M10 14a4 4 0 0 0 5.7 0l3.5-3.5a4 4 0 0 0-5.7-5.7L12 6.3"/><path d="M14 10a4 4 0 0 0-5.7 0l-3.5 3.5a4 4 0 0 0 5.7 5.7L12 17.7"/></svg>
          <span>www.lanternmeet.example</span>
        </li>
      </ul>
    </div>
  </section>

  <section class="card card-back">
    <div class="back-name">The Lantern<br>Gathering</div>
  </section>
</main>
</body>
</html>
```